Business card design needed

The company name is Pellwick Architects. We are an architectural company based in Melbourne,Australia that has a mix of client base from health care, commercial office, aged care, multi-residential, single residential and retail. Design type is contemporary.

Suggest the base colours need to be black and white. Please leave an area on the back of the card available for handwritten notes.

Target Market(s)

Generally corporate, aged 30 to 65

Industry/Entity Type

Residential

Contact Information for Business Card

Pellwick Architects
Dane Pellwick
7 Horbury Street
Northvale VIC 3059
T (03) 9572 4016
M 0431 607 295
E dp@pellwickarc.com.au

Logo Text

PA

Logo styles of interest
Emblem Logo
Abstract Logo
Lettermark Logo
Requirements
Must have
• I am having trouble attaching a sketch so would really appreciate your effort to try the following brief.

Black and White (B&W)
Would like different card cutout profile. Logo Example, use the half circle curve of the G to form the left edge of the card with no margin. The A is to sit inside the G, connected to the G by its horizontal. The A has its cross bar and lower right leg removed. Card in black, text in white.

Back of card to be black text on white background with services provided.

Client Focused Service
Architecture and Design
Functional Planning
Town Planning
Feasability Studies
Contract Documentation
Contract Administration
Project Management

Simple elegant text, Ariel or similar
Nice to have
• Integrated logo and card cut-out.

Card base black on front, white on back
Should not have
• Too many colours
Fussy details

```html
<!DOCTYPE html>
<html lang="en">
<head>
<meta charset="utf-8">
<title>Pellwick Architects – Business Card</title>
<link rel="stylesheet" href="https://fonts.googleapis.com/css2?family=Jost:wght@400;500&display=swap">
<style>
  :root {
    --stage: #2b2b2b;
    --card: #f7f7f7;
    --brand-blue: #2b3a96;
    --ink-grey: #4a4a4a;
    --rule-grey: #b9b9b9;
    --card-w: 620px;
    --card-h: 378px;
  }
  * { box-sizing: border-box; margin: 0; padding: 0; }
  html, body {
    width: 1200px; height: 900px; overflow: hidden;
    background: var(--stage);
    font-family: "Jost", Arial, sans-serif;
  }
  .canvas { position: relative; width: 1200px; height: 900px; }

  .card {
    position: absolute;
    width: var(--card-w); height: var(--card-h);
    background: var(--card);
    box-shadow: 0 12px 30px rgba(0,0,0,.45);
    overflow: hidden;
  }
  .card--back  { left: 150px; top: 40px;  border-radius: 6px 189px 189px 6px; }
  .card--front { left: 430px; top: 482px; border-radius: 189px 6px 6px 189px; }

  /* Back of card */
  .back-brand {
    position: absolute; left: 48px; top: 48px;
    display: flex; align-items: center; gap: 12px;
  }
  .back-brand__dot {
    width: 34px; height: 34px; border-radius: 50%;
    border: 5px solid var(--brand-blue);
  }
  .back-brand__name {
    font-size: 24px; font-weight: 400; color: var(--brand-blue);
    letter-spacing: 1px;
  }
  .services { position: absolute; left: 48px; top: 112px; color: var(--ink-grey); }
  .services__title { font-size: 22px; font-weight: 500; margin-bottom: 8px; }
  .services__list { list-style: none; }
  .services__list li {
    font-size: 18px; line-height: 26px; padding-left: 22px; position: relative;
  }
  .services__list li::before {
    content: ""; position: absolute; left: 4px; top: 10px;
    width: 7px; height: 7px; border-radius: 50%; background: var(--ink-grey);
  }

  /* Front of card */
  .front-mark {
    position: absolute; left: 34px; top: 39px;
    width: 300px; height: 300px; border-radius: 50%;
    border: 14px solid var(--brand-blue);
    display: flex; align-items: center; justify-content: center;
  }
  .front-mark__name {
    font-size: 44px; font-weight: 400; color: var(--brand-blue); letter-spacing: 1px;
  }
  .contact {
    position: absolute; right: 34px; top: 56px; width: 240px;
    text-align: right; color: var(--ink-grey);
  }
  .contact__name { font-size: 21px; font-weight: 500; color: var(--brand-blue); margin-bottom: 10px; }
  .contact__rule { height: 1px; background: var(--rule-grey); margin: 8px 0; }
  .contact__list { list-style: none; }
  .contact__list li {
    display: flex; justify-content: flex-end; align-items: center; gap: 10px;
    font-size: 16px; line-height: 24px;
  }
  .contact__list svg { width: 14px; height: 14px; fill: #8a8a8a; flex: none; }
  .contact__list .no-icon { padding-right: 24px; }
  .contact__company {
    margin-top: 18px; font-size: 24px; font-weight: 400;
    color: var(--brand-blue); letter-spacing: 1px;
  }
</style>
</head>
<body>
<main class="canvas">

  <section class="card card--back" aria-label="Back of card">
    <div class="back-brand">
      <span class="back-brand__dot"></span>
      <span class="back-brand__name">Pellwick Architects</span>
    </div>
    <div class="services">
      <h2 class="services__title">Client Focused Service</h2>
      <ul class="services__list">
        <li>Architecture + Design</li>
        <li>Functional Planning</li>
        <li>Town Planning</li>
        <li>Feasibility Studies</li>
        <li>Contract Documentation</li>
        <li>Contract Administration</li>
        <li>Project Management</li>
      </ul>
    </div>
  </section>

  <section class="card card--front" aria-label="Front of card">
    <div class="front-mark">
      <span class="front-mark__name">Pellwick</span>
    </div>
    <div class="contact">
      <h1 class="contact__name">Dane Pellwick</h1>
      <div class="contact__rule"></div>
      <ul class="contact__list">
        <li>7 Horbury Street,
          <svg viewBox="0 0 14 14" aria-hidden="true"><path d="M7 0a5 5 0 0 0-5 5c0 3.5 5 9 5 9s5-5.5 5-9a5 5 0 0 0-5-5zm0 7a2 2 0 1 1 0-4 2 2 0 0 1 0 4z"/></svg>
        </li>
        <li class="no-icon">Northvale VIC 3059</li>
        <li>(03) 9572 4016
          <svg viewBox="0 0 14 14" aria-hidden="true"><path d="M3 1l2 0 1 3-1.5 1a8 8 0 0 0 4.5 4.5L10 8l3 1v2a2 2 0 0 1-2 2C5.5 13 1 8.5 1 3a2 2 0 0 1 2-2z"/></svg>
        </li>
        <li>0431 607 295
          <svg viewBox="0 0 14 14" aria-hidden="true"><path d="M4 0h6a1 1 0 0 1 1 1v12a1 1 0 0 1-1 1H4a1 1 0 0 1-1-1V1a1 1 0 0 1 1-1zm0 2v9h6V2z"/></svg>
        </li>
        <li>dp@pellwickarc.com.au
          <svg viewBox="0 0 14 14" aria-hidden="true"><path d="M0 3h14v8H0zm1 1l6 4 6-4v-0.5H1z"/></svg>
        </li>
      </ul>
      <div class="contact__rule"></div>
      <p class="contact__company">Pellwick Architects</p>
    </div>
  </section>

</main>
</body>
</html>
```